VB Heating & Cooling / 2018 Brenk Moviro Medium Roof / 148"wb

Customer is looking for a new design on his new 2018 brenk moviro medium roof 148"wb van. This will be a Full Wrap.

Attached is: >Customers logo
> Template for the van he has (You don't have to use this exact one for the proof)

Please include: > Slogan- Quality work at reasonable prices
>(555) 019-4821
>Services- Repairs, installation, maintenance, water heaters, indoor air quality
>Residential & Commercial

```html
<!DOCTYPE html>
<html lang="en">
<head>
<meta charset="utf-8">
<title>VB Heating &amp; Cooling – Brenk Moviro Full Wrap</title>
<link rel="stylesheet" href="https://fonts.googleapis.com/css2?family=EB+Garamond:ital,wght@1,500&family=Montserrat:ital,wght@0,600;0,700;0,800;1,600&display=swap">
<style>
  :root {
    --page: #e9e9eb;
    --wrap-white: #f4f5f7;
    --sky: #6fa4dc;
    --royal: #2f5fa8;
    --navy: #1f3470;
    --gold: #e2a424;
    --orange: #ec8a1c;
    --ember: #e5531a;
    --slogan: #d9581c;
    --charcoal: #2b2c2f;
    --tyre: #1c1c1e;
    --glass: #25272c;
  }
  html, body { margin: 0; padding: 0; }
  body {
    width: 1200px; height: 3419px; overflow: hidden;
    background: var(--page);
    font-family: "Montserrat", sans-serif;
  }
  .wrap-view { display: block; width: 1200px; }
  .view-side { height: 900px; }
  .view-rear { height: 800px; }
  .view-front { height: 819px; }
  .slogan { font-family: "EB Garamond", serif; font-style: italic; font-weight: 500; fill: var(--slogan); }
  .slogan-light { fill: #ffffff; }
  .service { font-weight: 600; font-size: 18px; fill: var(--ember); }
  .service-light { fill: #ffffff; font-style: italic; }
  .bullet { fill: none; stroke: var(--royal); stroke-width: 1.6; }
  .bullet-light { stroke: #ffffff; }
  .brand-name { font-weight: 800; fill: var(--royal); letter-spacing: 1px; }
  .market { font-weight: 600; font-style: italic; fill: #ffffff; }
  .market-dark { fill: var(--navy); }
  .phone { font-weight: 700; fill: var(--ember); }
  .phone-dark { fill: var(--royal); }
</style>
</head>
<body>

<svg width="0" height="0" style="position:absolute" aria-hidden="true">
  <defs>
    <linearGradient id="grad-sky" x1="0" y1="0" x2="1" y2="0">
      <stop offset="0" stop-color="#8fbdea"/><stop offset="1" stop-color="#3f73bf"/>
    </linearGradient>
    <linearGradient id="grad-sun" x1="0" y1="0" x2="1" y2="1">
      <stop offset="0" stop-color="#f2b632"/><stop offset="1" stop-color="#e0901c"/>
    </linearGradient>
    <linearGradient id="grad-fire" x1="0" y1="0" x2="0" y2="1">
      <stop offset="0" stop-color="#f09a22"/><stop offset="1" stop-color="#e5531a"/>
    </linearGradient>
    <linearGradient id="grad-navy" x1="0" y1="0" x2="1" y2="0">
      <stop offset="0" stop-color="#2a4c96"/><stop offset="1" stop-color="#1b2b5e"/>
    </linearGradient>
    <linearGradient id="grad-gauges" x1="0" y1="0" x2="1" y2="0">
      <stop offset="0" stop-color="#e0453a"/><stop offset=".5" stop-color="#f0c040"/><stop offset="1" stop-color="#3a7fd0"/>
    </linearGradient>
    <clipPath id="clip-side-body">
      <path d="M40,230 Q50,188 120,184 L640,178 Q770,178 880,238 L1080,378 Q1160,408 1170,450 L1175,560 L1165,600 L40,600 L28,500 Z"/>
    </clipPath>
  </defs>
</svg>

<!-- Driver side -->
<svg class="wrap-view view-side" viewBox="0 0 1200 900" role="group" aria-label="Driver side wrap">
  <g class="side-panel">
    <g clip-path="url(#clip-side-body)">
      <rect x="0" y="150" width="1200" height="470" fill="var(--wrap-white)"/>
      <path d="M0,150 L660,150 Q640,190 600,200 L0,210 Z" fill="url(#grad-sky)"/>
      <path d="M640,150 L1200,150 L1200,420 L1100,390 Q900,230 760,200 L620,205 Z" fill="url(#grad-sun)"/>
      <path d="M900,250 L1200,330 L1200,440 L1090,420 Z" fill="url(#grad-navy)"/>
      <path d="M0,395 L1200,478 L1200,492 L0,405 Z" fill="var(--orange)"/>
      <path d="M0,410 L480,412 Q520,415 560,440 L0,520 Z" fill="url(#grad-fire)"/>
      <path d="M360,470 Q520,430 700,470 L1200,505 L1200,520 L700,488 Q520,455 360,492 Z" fill="var(--gold)"/>
      <path d="M480,520 Q620,490 900,500 L1200,512 L1200,530 L900,520 Q620,510 500,540 Z" fill="var(--royal)"/>
      <path d="M360,540 L900,545 L880,590 L380,590 Z" fill="var(--sky)"/>
      <path d="M300,550 L560,550 L540,600 L300,600 Z" fill="var(--gold)"/>
      <rect x="0" y="530" width="1200" height="70" fill="var(--charcoal)" opacity=".85"/>
      <path d="M735,255 Q800,250 880,262 L920,410 L740,410 Z" fill="var(--glass)"/>
    </g>
    <circle cx="270" cy="590" r="72" fill="var(--tyre)"/>
    <circle cx="985" cy="595" r="72" fill="var(--tyre)"/>
    <circle cx="270" cy="590" r="44" fill="#d9dadd"/>
    <circle cx="985" cy="595" r="44" fill="#d9dadd"/>
  </g>
  <text class="slogan" x="215" y="232" font-size="27" transform="rotate(1.5 215 232)">Quality Work at reasonable prices !</text>
  <g class="services" transform="translate(196,263)">
    <circle class="bullet" cx="0" cy="-6" r="5"/><text class="service" x="14" y="0">Services</text>
    <circle class="bullet" cx="0" cy="15" r="5"/><text class="service" x="14" y="21">Repairs</text>
    <circle class="bullet" cx="0" cy="36" r="5"/><text class="service" x="14" y="42">installation</text>
    <circle class="bullet" cx="0" cy="57" r="5"/><text class="service" x="14" y="63">Maintenance</text>
    <circle class="bullet" cx="0" cy="78" r="5"/><text class="service" x="14" y="84">water heaters</text>
    <circle class="bullet" cx="0" cy="99" r="5"/><text class="service" x="14" y="105">indoor air quality</text>
  </g>
  <text class="brand-name" x="350" y="312" font-size="40">VB HEATING</text>
  <text class="brand-name" x="375" y="358" font-size="40">&amp; COOLING</text>
  <rect x="465" y="372" width="95" height="48" rx="4" fill="url(#grad-gauges)" role="img" aria-label="HVAC gauge manifold illustration"/>
  <text class="market" x="110" y="440" font-size="21">Residential &amp; Commercial</text>
  <text class="phone" x="770" y="432" font-size="22">(555) 019 - 4821</text>
</svg>

<!-- Passenger side -->
<svg class="wrap-view view-side" viewBox="0 0 1200 900" role="group" aria-label="Passenger side wrap">
  <g class="side-panel" transform="translate(1200,0) scale(-1,1)">
    <g clip-path="url(#clip-side-body)">
      <rect x="0" y="150" width="1200" height="470" fill="var(--wrap-white)"/>
      <path d="M0,150 L660,150 Q640,190 600,200 L0,210 Z" fill="url(#grad-sky)"/>
      <path d="M640,150 L1200,150 L1200,420 L1100,390 Q900,230 760,200 L620,205 Z" fill="url(#grad-sun)"/>
      <path d="M900,250 L1200,330 L1200,440 L1090,420 Z" fill="url(#grad-navy)"/>
      <path d="M0,395 L1200,478 L1200,492 L0,405 Z" fill="var(--orange)"/>
      <path d="M0,410 L480,412 Q520,415 560,440 L0,520 Z" fill="url(#grad-fire)"/>
      <path d="M360,470 Q520,430 700,470 L1200,505 L1200,520 L700,488 Q520,455 360,492 Z" fill="var(--gold)"/>
      <path d="M480,520 Q620,490 900,500 L1200,512 L1200,530 L900,520 Q620,510 500,540 Z" fill="var(--royal)"/>
      <path d="M360,540 L900,545 L880,590 L380,590 Z" fill="var(--sky)"/>
      <path d="M300,550 L560,550 L540,600 L300,600 Z" fill="var(--gold)"/>
      <rect x="0" y="530" width="1200" height="70" fill="var(--charcoal)" opacity=".85"/>
      <path d="M735,255 Q800,250 880,262 L920,410 L740,410 Z" fill="var(--glass)"/>
    </g>
    <circle cx="270" cy="590" r="72" fill="var(--tyre)"/>
    <circle cx="985" cy="595" r="72" fill="var(--tyre)"/>
    <circle cx="270" cy="590" r="44" fill="#d9dadd"/>
    <circle cx="985" cy="595" r="44" fill="#d9dadd"/>
  </g>
  <text class="slogan" x="610" y="232" font-size="27" transform="rotate(-1.5 610 232)">Quality Work at reasonable prices !</text>
  <g class="services" transform="translate(890,263)">
    <circle class="bullet" cx="0" cy="-6" r="5"/><text class="service" x="14" y="0">Services</text>
    <circle class="bullet" cx="0" cy="15" r="5"/><text class="service" x="14" y="21">Repairs</text>
    <circle class="bullet" cx="0" cy="36" r="5"/><text class="service" x="14" y="42">installation</text>
    <circle class="bullet" cx="0" cy="57" r="5"/><text class="service" x="14" y="63">Maintenance</text>
    <circle class="bullet" cx="0" cy="78" r="5"/><text class="service" x="14" y="84">water heaters</text>
    <circle class="bullet" cx="0" cy="99" r="5"/><text class="service" x="14" y="105">indoor air quality</text>
  </g>
  <text class="brand-name" x="495" y="305" font-size="40">VB HEATING</text>
  <text class="brand-name" x="520" y="351" font-size="40">&amp; COOLING</text>
  <rect x="600" y="365" width="95" height="48" rx="4" fill="url(#grad-gauges)" role="img" aria-label="HVAC gauge manifold illustration"/>
  <text class="market" x="833" y="432" font-size="21">Residential &amp; Commercial</text>
  <text class="phone" x="255" y="436" font-size="22">(555) 019 - 4821</text>
</svg>

<!-- Rear doors -->
<svg class="wrap-view view-rear" viewBox="0 0 1200 800" role="group" aria-label="Rear doors wrap">
  <g class="rear-panel">
    <path d="M305,75 Q600,55 895,75 L905,600 L295,600 Z" fill="var(--wrap-white)"/>
    <path d="M305,75 Q600,55 895,75 L892,160 Q600,145 308,160 Z" fill="url(#grad-sky)"/>
    <rect x="296" y="395" width="608" height="12" fill="var(--orange)"/>
    <rect x="296" y="407" width="608" height="185" fill="url(#grad-fire)"/>
    <line x1="598" y1="75" x2="598" y2="592" stroke="#b9bcc2" stroke-width="2"/>
    <rect x="285" y="592" width="630" height="110" rx="10" fill="var(--charcoal)"/>
    <rect x="660" y="620" width="135" height="30" fill="#e8eef4"/>
    <rect x="285" y="225" width="28" height="150" rx="4" fill="#c2262d"/>
    <rect x="887" y="225" width="28" height="150" rx="4" fill="#c2262d"/>
  </g>
  <text class="slogan slogan-light" x="600" y="124" font-size="26" text-anchor="middle">Quality Work at reasonable prices</text>
  <text class="brand-name" x="600" y="228" font-size="46" text-anchor="middle">VB HEATING</text>
  <text class="brand-name" x="600" y="282" font-size="46" text-anchor="middle">&amp; COOLING</text>
  <rect x="545" y="298" width="110" height="58" rx="4" fill="url(#grad-gauges)" role="img" aria-label="HVAC gauge manifold illustration"/>
  <text class="market market-dark" x="595" y="388" font-size="17" text-anchor="middle">Residential &amp; Commercial</text>
  <g class="services" transform="translate(358,465)">
    <circle class="bullet bullet-light" cx="0" cy="-6" r="5"/><text class="service service-light" x="12" y="0">Services</text>
    <circle class="bullet bullet-light" cx="0" cy="15" r="5"/><text class="service service-light" x="12" y="21">Repairs</text>
    <circle class="bullet bullet-light" cx="0" cy="36" r="5"/><text class="service service-light" x="12" y="42">installation</text>
    <circle class="bullet bullet-light" cx="0" cy="57" r="5"/><text class="service service-light" x="12" y="63">Maintenance</text>
    <circle class="bullet bullet-light" cx="0" cy="78" r="5"/><text class="service service-light" x="12" y="84">water heaters</text>
    <circle class="bullet bullet-light" cx="0" cy="99" r="5"/><text class="service service-light" x="12" y="105">indoor air quality</text>
  </g>
  <text class="phone phone-dark" x="735" y="525" font-size="32" text-anchor="middle">(555) 019 - 4821</text>
</svg>

<!-- Front -->
<svg class="wrap-view view-front" viewBox="0 0 1200 819" role="group" aria-label="Front wrap">
  <g class="front-panel">
    <path d="M330,70 Q600,45 870,70 L900,380 L935,640 Q600,660 265,640 L300,380 Z" fill="url(#grad-navy)"/>
    <path d="M330,70 Q600,45 870,70 L880,150 Q600,135 320,150 Z" fill="url(#grad-sun)"/>
    <path d="M320,115 Q600,100 880,115 L870,380 Q600,370 330,380 Z" fill="var(--glass)"/>
    <path d="M370,385 Q600,370 830,385 L800,470 Q600,500 400,470 Z" fill="var(--wrap-white)"/>
    <path d="M370,385 Q600,370 830,385 L815,400 Q600,388 385,400 Z" fill="var(--orange)"/>
    <rect x="420" y="520" width="360" height="120" rx="14" fill="var(--charcoal)"/>
    <rect x="265" y="640" width="670" height="110" rx="12" fill="var(--charcoal)"/>
    <rect x="500" y="690" width="185" height="32" fill="#e8eef4"/>
  </g>
  <text class="brand-name" x="600" y="432" font-size="24" text-anchor="middle">VB HEATING</text>
  <text class="brand-name" x="600" y="458" font-size="24" text-anchor="middle">&amp; COOLING</text>
  <rect x="572" y="464" width="56" height="14" rx="2" fill="url(#grad-gauges)" role="img" aria-label="HVAC gauge manifold illustration"/>
</svg>

</body>
</html>
```